Dorsey K. Wendell Business Card

We need a business card for our company Dorsey K. Wendell Heating & Plumbing to be distributed to potential customers. It should follow the color scheme of our logo and have a modern upscale and masculine look.

The logo is attached and the info below should also be included:

5187 W. Cedar Brook Rd.
Elmridge, PA 17588

Russell T. Wendell
(717) 592-0817
russelltwendell@fernmail.net
dorseykwendell.net
PA #093148

Industry/Entity Type

Business

Contact Information for Business Card

5187 W. Cedar Brook Rd.
Elmridge, PA 17588

Russell T. Wendell
(717) 592-0817
russelltwendell@fernmail.net
dorseykwendell.net
PA #093148

Colors

Designer to choose colors to be used in the design.

Requirements
Must have
• Information above included

```html
<!DOCTYPE html>
<html lang="en">
<head>
<meta charset="utf-8">
<title>Dorsey K. Wendell Business Card</title>
<link href="https://fonts.googleapis.com/css2?family=Karla:wght@400;500;700;800&display=swap" rel="stylesheet">
<style>
  :root {
    --navy: #27589a;
    --sky: #8fd6f4;
    --lime: #9bcb3b;
    --paper: #ffffff;
    --ink: #2c2c2c;
    --backdrop: #ececea;
  }
  * { margin: 0; padding: 0; box-sizing: border-box; }
  html, body {
    width: 1200px;
    height: 1200px;
    overflow: hidden;
    background: var(--backdrop);
    font-family: "Karla", Arial, sans-serif;
  }
  .canvas {
    position: relative;
    width: 1200px;
    height: 1200px;
  }
  .card {
    position: absolute;
    left: 220px;
    width: 760px;
    height: 434px;
    background: var(--paper);
    box-shadow: 0 6px 18px rgba(0,0,0,0.18);
    overflow: hidden;
  }
  .card--front { top: 122px; }
  .card--back { top: 630px; }
  .card__bands {
    position: absolute;
    inset: 0;
    width: 100%;
    height: 100%;
  }
  .band--navy { fill: var(--navy); }
  .band--sky { fill: var(--sky); }

  .brand {
    position: absolute;
    display: flex;
    align-items: center;
    gap: 16px;
  }
  .brand__mark {
    width: 54px;
    height: 54px;
    background: var(--lime);
    flex: none;
  }
  .brand__name {
    font-weight: 800;
    line-height: 1.05;
    letter-spacing: 0.5px;
    text-transform: uppercase;
    white-space: nowrap;
  }
  .brand__name span { display: block; }
  .card--front .brand {
    left: 50%;
    top: 50%;
    transform: translate(-50%, -50%);
  }
  .card--front .brand__mark { width: 72px; height: 72px; }
  .card--front .brand__name { color: var(--paper); font-size: 38px; }
  .card--front .brand__name .brand__trade { font-size: 21px; letter-spacing: 2px; }

  .card--back .brand { left: 62px; top: 84px; }
  .card--back .brand__name { color: var(--navy); font-size: 28px; }
  .card--back .brand__name .brand__trade { font-size: 16px; letter-spacing: 1.6px; }

  .contact-person {
    position: absolute;
    left: 60px;
    top: 296px;
  }
  .contact-person__name {
    color: var(--navy);
    font-weight: 700;
    font-size: 25px;
    line-height: 1.2;
  }
  .contact-person__phone {
    color: var(--ink);
    font-size: 20px;
    margin-top: 4px;
  }
  .contact-details {
    position: absolute;
    right: 60px;
    top: 224px;
    text-align: right;
    list-style: none;
    color: var(--ink);
    font-size: 20px;
    line-height: 1.38;
    white-space: nowrap;
  }
</style>
</head>
<body>
<main class="canvas">

  <section class="card card--front" aria-label="Card front">
    <svg class="card__bands" viewBox="0 0 760 434" aria-hidden="true">
      <polygon class="band--sky" points="502,0 760,0 760,52 450,52"/>
      <polygon class="band--navy" points="0,72 430,72 450,52 760,52 760,362 330,362 310,382 0,382"/>
      <polygon class="band--sky" points="0,382 310,382 258,434 0,434"/>
    </svg>
    <div class="brand">
      <div class="brand__mark"></div>
      <p class="brand__name"><span>Dorsey K. Wendell</span><span class="brand__trade">Heating &amp; Plumbing</span></p>
    </div>
  </section>

  <section class="card card--back" aria-label="Card back">
    <svg class="card__bands" viewBox="0 0 760 434" aria-hidden="true">
      <polygon class="band--sky" points="560,0 760,0 760,38 552,38"/>
      <polygon class="band--navy" points="0,0 570,0 545,56 0,56"/>
      <rect class="band--sky" x="0" y="392" width="760" height="42"/>
      <polygon class="band--navy" points="300,374 760,374 760,434 272,434"/>
    </svg>
    <div class="brand">
      <div class="brand__mark"></div>
      <p class="brand__name"><span>Dorsey K. Wendell</span><span class="brand__trade">Heating &amp; Plumbing</span></p>
    </div>
    <div class="contact-person">
      <p class="contact-person__name">Russell T. Wendell</p>
      <p class="contact-person__phone">(717) 592-0817</p>
    </div>
    <ul class="contact-details">
      <li>5187 W. Cedar Brook Rd.</li>
      <li>Elmridge, PA 17588</li>
      <li>russelltwendell@fernmail.net</li>
      <li>dorseykwendell.net</li>
      <li>PA #093148</li>
    </ul>
  </section>

</main>
</body>
</html>
```